Maplegate Chapel Business Cards and Stationary
Maplegate Chapel
Maplegate Chapel Business Cards and Stationary - Religion and Spirituality
Creative Brief
Professional
Rev. Harold J Lindqvist
Sr. Pastor
27 Tamsin Lane Harlow Bay, FL 32190
pastorhal@maplegatefl.example
www.maplegatefl.example
Even though my name is on the card we need to be able to make cards for all of our leaders.
Back of card should list services: Sunday Mornings @ 9 AM & 11 AM Dawn Watchful Devotion (DWD) Mon - Fri @ 7AM Lumen - Young Adults Mon @ 7PM HELM - Midweek Service Tues @ 6:30 PM Women's Bible Study - Wed. 10:30 AM The FORGE - Youth Ministry Wed @ 6:45 PM

```html
<!DOCTYPE html>
<html lang="en">
<head>
<meta charset="utf-8">
<title>Maplegate Chapel Stationery</title>
<link rel="stylesheet" href="https://fonts.googleapis.com/css2?family=Cinzel:wght@600&family=Open+Sans:wght@400;600;700&display=swap">
<style>
  :root{
    --backdrop:#e7e4df;
    --paper:#ffffff;
    --navy:#1e4459;
    --navy-light:#2c5b72;
    --olive:#6b7f35;
    --ink:#2f3a40;
    --muted:#6d777c;
    --mist:#dfe5e8;
    --fold:#d9dde0;
  }
  *{box-sizing:border-box;margin:0;padding:0}
  html,body{width:1200px;height:811px;overflow:hidden;background:var(--backdrop)}
  body{position:relative;font-family:"Open Sans",Arial,sans-serif;color:var(--ink)}

  .piece{position:absolute;background:var(--paper);overflow:hidden;box-shadow:0 2px 8px rgba(0,0,0,.18)}
  .swoosh{position:absolute;left:0;bottom:0;width:100%;display:block}
  .watermark{position:absolute;border-radius:6px;
    background:linear-gradient(120deg,rgba(223,229,232,0) 0%,#e9edef 35%,#e2e7ea 65%,rgba(223,229,232,0) 100%)}
  .wordmark{position:absolute;font-family:"Cinzel",Georgia,serif;font-weight:600;color:var(--navy);
    letter-spacing:.03em;line-height:1;display:flex;align-items:center;gap:5px;white-space:nowrap}
  .wordmark .dot{width:6px;height:6px;border-radius:50%;background:var(--navy);flex:none}
  .contact{position:absolute;color:var(--muted);line-height:1.5;white-space:nowrap}

  /* envelope back (flap) */
  .envelope-back{left:30px;top:60px;width:360px;height:170px}
  .envelope-back .flap{position:absolute;left:0;top:0;width:100%;height:100%}
  .envelope-back .wordmark{left:50%;top:62px;transform:translateX(-50%);font-size:11px}

  /* long envelopes */
  .envelope{width:360px;height:170px}
  .envelope-a{left:30px;top:300px}
  .envelope-b{left:30px;top:540px}
  .envelope .wordmark{left:16px;top:16px;font-size:11px}
  .envelope .contact{left:16px;top:34px;font-size:6.5px}
  .envelope .watermark{left:170px;top:40px;width:150px;height:100px}
  .envelope-a .swoosh{height:46px}
  .envelope-b .swoosh{height:66px}

  /* letterheads */
  .letterhead{top:30px;width:300px;height:424px}
  .letterhead-a{left:470px}
  .letterhead-b{left:820px}
  .letterhead .wordmark{right:24px;top:24px;font-size:13px}
  .letterhead .watermark{left:60px;top:250px;width:170px;height:110px}
  .letterhead .contact{right:24px;top:300px;font-size:7px;text-align:right}
  .letterhead-a .swoosh{height:80px}
  .letterhead-b .swoosh{height:58px}

  /* business cards */
  .card{width:245px;height:140px}
  .front-a{left:535px;top:490px}
  .back-a{left:810px;top:490px}
  .front-b{left:535px;top:650px}
  .back-b{left:810px;top:650px}
  .card .wordmark{left:12px;top:12px;font-size:10px}
  .card .swoosh{height:28px}
  .card-front .watermark{left:135px;top:34px;width:95px;height:72px}
  .card-front .person{position:absolute;left:12px;top:34px}
  .card-front .person h2{font-size:9px;font-weight:700;color:var(--navy);line-height:1.3}
  .card-front .person p{font-size:6.5px;color:var(--muted)}
  .card-front .contact{left:12px;top:60px;font-size:6px;line-height:1.45}

  .card-back .services{position:absolute;left:12px;top:28px;width:221px;border-collapse:collapse;font-size:5.6px;line-height:1.3}
  .card-back .services th{background:var(--navy);color:#fff;font-weight:600;text-align:left;padding:1.5px 4px}
  .card-back .services td{padding:1.2px 4px;border-bottom:1px solid var(--mist);white-space:nowrap}
  .card-back .services td:last-child{text-align:right;color:var(--navy);font-weight:600}
</style>
</head>
<body>

<svg width="0" height="0" style="position:absolute" aria-hidden="true">
  <defs>
    <symbol id="band" viewBox="0 0 100 30" preserveAspectRatio="none">
      <path d="M0 14 C30 4 62 24 100 8 L100 30 L0 30Z" fill="#2c5b72"/>
      <path d="M0 17 C30 7 62 27 100 11 L100 30 L0 30Z" fill="#1e4459"/>
      <path d="M0 11 C30 1 62 21 100 5" fill="none" stroke="#6b7f35" stroke-width="2" vector-effect="non-scaling-stroke"/>
    </symbol>
  </defs>
</svg>

<section class="piece envelope-back">
  <svg class="flap" viewBox="0 0 360 170" preserveAspectRatio="none" aria-hidden="true">
    <path d="M0 0 L180 82 L360 0" fill="none" stroke="#d9dde0" stroke-width="1"/>
    <path d="M0 170 L150 96 M360 170 L210 96" fill="none" stroke="#e4e7e9" stroke-width="1"/>
  </svg>
  <div class="wordmark"><span class="dot"></span>Maplegate Chapel</div>
</section>

<section class="piece envelope envelope-a">
  <div class="watermark" role="img" aria-label="Faint cross and globe watermark"></div>
  <div class="wordmark"><span class="dot"></span>Maplegate Chapel</div>
  <div class="contact">27 Tamsin Lane<br>Harlow Bay, FL 32190</div>
  <svg class="swoosh" aria-hidden="true"><use href="#band"/></svg>
</section>

<section class="piece envelope envelope-b">
  <div class="watermark" role="img" aria-label="Faint cross and globe watermark"></div>
  <div class="wordmark"><span class="dot"></span>Maplegate Chapel</div>
  <div class="contact">27 Tamsin Lane<br>Harlow Bay, FL 32190</div>
  <svg class="swoosh" aria-hidden="true"><use href="#band"/></svg>
</section>

<section class="piece letterhead letterhead-a">
  <div class="watermark" role="img" aria-label="Faint cross and globe watermark"></div>
  <div class="wordmark"><span class="dot"></span>Maplegate Chapel</div>
  <div class="contact">
    27 Tamsin Lane Harlow Bay, FL 32190<br>
    pastorhal@maplegatefl.example<br>
    www.maplegatefl.example
  </div>
  <svg class="swoosh" aria-hidden="true"><use href="#band"/></svg>
</section>

<section class="piece letterhead letterhead-b">
  <div class="watermark" role="img" aria-label="Faint cross and globe watermark"></div>
  <div class="wordmark"><span class="dot"></span>Maplegate Chapel</div>
  <div class="contact">
    27 Tamsin Lane Harlow Bay, FL 32190<br>
    pastorhal@maplegatefl.example<br>
    www.maplegatefl.example
  </div>
  <svg class="swoosh" aria-hidden="true"><use href="#band"/></svg>
</section>

<section class="piece card card-front front-a">
  <div class="watermark" role="img" aria-label="Faint cross and globe watermark"></div>
  <div class="wordmark"><span class="dot"></span>Maplegate Chapel</div>
  <div class="person"><h2>Rev. Harold J Lindqvist</h2><p>Sr. Pastor</p></div>
  <div class="contact">
    27 Tamsin Lane Harlow Bay, FL 32190<br>
    pastorhal@maplegatefl.example<br>
    www.maplegatefl.example
  </div>
  <svg class="swoosh" aria-hidden="true"><use href="#band"/></svg>
</section>

<section class="piece card card-back back-a">
  <div class="wordmark"><span class="dot"></span>Maplegate Chapel</div>
  <table class="services">
    <tr><th>Service</th><th></th></tr>
    <tr><td>Sunday Mornings</td><td>9 AM &amp; 11 AM</td></tr>
    <tr><td>Dawn Watchful Devotion (DWD)</td><td>Mon - Fri 7 AM</td></tr>
    <tr><td>Lumen - Young Adults</td><td>Mon 7 PM</td></tr>
    <tr><td>HELM - Midweek Service</td><td>Tues 6:30 PM</td></tr>
    <tr><td>Women's Bible Study</td><td>Wed 10:30 AM</td></tr>
    <tr><td>The FORGE - Youth Ministry</td><td>Wed 6:45 PM</td></tr>
  </table>
  <svg class="swoosh" aria-hidden="true"><use href="#band"/></svg>
</section>

<section class="piece card card-front front-b">
  <div class="watermark" role="img" aria-label="Faint cross and globe watermark"></div>
  <div class="wordmark"><span class="dot"></span>Maplegate Chapel</div>
  <div class="person"><h2>Rev. Harold J Lindqvist</h2><p>Sr. Pastor</p></div>
  <div class="contact">
    27 Tamsin Lane Harlow Bay, FL 32190<br>
    pastorhal@maplegatefl.example<br>
    www.maplegatefl.example
  </div>
  <svg class="swoosh" aria-hidden="true"><use href="#band"/></svg>
</section>

<section class="piece card card-back back-b">
  <div class="wordmark"><span class="dot"></span>Maplegate Chapel</div>
  <table class="services">
    <tr><th>Service</th><th></th></tr>
    <tr><td>Sunday Mornings</td><td>9 AM &amp; 11 AM</td></tr>
    <tr><td>Dawn Watchful Devotion (DWD)</td><td>Mon - Fri 7 AM</td></tr>
    <tr><td>Lumen - Young Adults</td><td>Mon 7 PM</td></tr>
    <tr><td>HELM - Midweek Service</td><td>Tues 6:30 PM</td></tr>
    <tr><td>Women's Bible Study</td><td>Wed 10:30 AM</td></tr>
    <tr><td>The FORGE - Youth Ministry</td><td>Wed 6:45 PM</td></tr>
  </table>
  <svg class="swoosh" aria-hidden="true"><use href="#band"/></svg>
</section>

</body>
</html>
```